依頼詳細
今回依頼するのは、500mlのビンの外箱です。

ビンの形状はワインボトルに似ています。

■依頼するビンの外箱のサイズは 高さ30cm×横7cm×奥行7cm の 細長い四角柱型。
■4面の中でデザイン箇所は、3面。1面は成分表示やお召し上がり方を記載します。
■ターゲットは20代~30代の女性向け
■商品の品質には絶対の自信があります。
■商品名は「コルダミナ」 Kordami
■ダイエット効果や、美容、健康に重点を置いた商品なので、デザインイメージは「美しい女性」。

記載項目
特に無し。
希望イメージ
シンプル 複雑
単色 カラフル
暗い 明るい
日常 高級
遊び心 厳粛
未来的 伝統的
女性的 男性的
希望する色
ゴールド、グリーン、シルバーなど。単色でもOK。
納品ファイル
• 高解像度JPG (.jpg)
• イラストレーター形式 (.ai)
補足説明
ビンのイメージを追加します。

色は水色で、形状は画像のものとほぼ同じです。ご参考までに・・。
■ 選んだ理由

素晴らしいデザインで、社内の中でも満場一致です!

■ 提案者全員のお礼・コメント

皆様、本当にありがとうございました。

初めての依頼でしたので、お時間を頂きましたが、大満足でした。

また是非ご参加をお待ちしております。

```html
<!DOCTYPE html>
<html lang="ja">
<head>
<meta charset="utf-8">
<title>コルダミナ 酵素ドリンク 外箱 展開面</title>
<link rel="stylesheet" href="https://fonts.googleapis.com/css2?family=Noto+Serif+JP:wght@500;700;900&family=Playfair+Display:wght@700&display=swap">
<style>
  :root {
    --stage: #f1efec;
    --wine-deep: #3e080b;
    --wine: #741316;
    --wine-light: #94241f;
    --gold-dark: #8f6a2a;
    --gold: #c9a456;
    --gold-light: #f0dc9e;
    --ink: #1a1010;
    --white: #ffffff;
  }
  * { margin: 0; padding: 0; box-sizing: border-box; }
  html, body {
    width: 1200px; height: 2992px; overflow: hidden;
    background: var(--stage);
  }
  .box-net {
    position: absolute; left: 20px; top: 66px;
    width: 1160px; height: 2860px;
    display: flex;
    box-shadow: 0 20px 60px rgba(0,0,0,.18);
  }
  .face {
    position: relative;
    width: 580px; height: 2860px;
    overflow: hidden;
    background: linear-gradient(180deg, var(--wine-deep) 0%, var(--wine) 20%, var(--wine-light) 46%, var(--wine) 74%, var(--wine-deep) 100%);
  }
  .face--side::after {
    content: ""; position: absolute; inset: 0;
    background: linear-gradient(90deg, rgba(0,0,0,.14), rgba(0,0,0,0) 40%);
    pointer-events: none;
  }
  .gold-band {
    position: absolute; left: 0; width: 100%;
    display: flex; align-items: center; justify-content: center;
    background: linear-gradient(180deg, var(--gold-dark) 0%, var(--gold-light) 42%, var(--gold) 70%, var(--gold-dark) 100%);
  }
  .gold-band--top { top: 0; height: 340px; }
  .gold-band--main { top: 1480px; height: 260px; }
  .black-strip {
    position: absolute; left: 0; width: 100%;
    background: var(--ink);
    display: flex; align-items: center; justify-content: center;
  }
  .black-strip--top { top: 340px; height: 64px; }
  .black-strip--main { top: 1740px; height: 76px; }
  .brand-latin {
    font-family: "Playfair Display", serif; font-weight: 700;
    color: var(--ink); letter-spacing: 1px; line-height: 1;
  }
  .gold-band--top .brand-latin { font-size: 104px; padding-top: 30px; }
  .gold-band--main .brand-latin { font-size: 122px; }
  .brand-kana {
    font-family: "Noto Serif JP", serif; font-weight: 700;
    color: var(--white); letter-spacing: 6px; line-height: 1;
  }
  .black-strip--top .brand-kana { font-size: 36px; }
  .black-strip--main .brand-kana { font-size: 46px; }
  .ornament { position: absolute; left: 0; width: 100%; }
  .ornament--top {
    top: 404px; height: 200px;
    background: radial-gradient(ellipse at 50% 0%, rgba(201,164,86,.35) 0%, rgba(116,19,22,0) 70%);
  }
  .ornament--upper {
    top: 1010px; height: 470px;
    background:
      radial-gradient(ellipse 60% 55% at 30% 70%, rgba(214,178,96,.75) 0%, rgba(214,178,96,0) 100%),
      radial-gradient(ellipse 60% 55% at 72% 60%, rgba(214,178,96,.7) 0%, rgba(214,178,96,0) 100%),
      linear-gradient(180deg, rgba(62,8,11,0) 0%, rgba(62,8,11,.55) 100%);
  }
  .ornament--lower {
    top: 1816px; height: 500px;
    background:
      radial-gradient(ellipse 60% 50% at 35% 25%, rgba(214,178,96,.65) 0%, rgba(214,178,96,0) 100%),
      radial-gradient(ellipse 55% 45% at 75% 45%, rgba(214,178,96,.5) 0%, rgba(214,178,96,0) 100%),
      linear-gradient(180deg, rgba(62,8,11,.55) 0%, rgba(62,8,11,0) 100%);
  }
  .ornament--bottom {
    top: 2600px; height: 260px;
    background: radial-gradient(ellipse 70% 60% at 40% 60%, rgba(150,40,36,.6) 0%, rgba(150,40,36,0) 100%);
  }
  .product-type {
    position: absolute; top: 640px; left: 0; width: 100%;
    text-align: center;
    font-family: "Noto Serif JP", serif; font-weight: 900;
    font-size: 58px; letter-spacing: 3px; color: var(--white);
  }
  .product-lead {
    position: absolute; top: 820px; left: 0; width: 100%;
    text-align: center;
    font-family: "Noto Serif JP", serif; font-weight: 700;
    font-size: 32px; line-height: 1.75; letter-spacing: 1px; color: var(--white);
  }
  .volume {
    position: absolute; top: 2420px; left: 0; width: 100%;
    text-align: center;
    font-family: "Noto Serif JP", serif; font-weight: 500;
    font-size: 50px; letter-spacing: 2px; color: var(--gold-light);
  }
</style>
</head>
<body>
  <div class="box-net">
    <section class="face face--front">
      <div class="gold-band gold-band--top"><span class="brand-latin">Kordami</span></div>
      <div class="black-strip black-strip--top"><span class="brand-kana">コルダミナ</span></div>
      <div class="ornament ornament--top" role="img" aria-label="金色のつる草の装飾模様"></div>
      <h1 class="product-type">酵素ドリンク</h1>
      <p class="product-lead">約100種類の野菜を<br>熟成発酵させた複合植物エキス</p>
      <div class="ornament ornament--upper" role="img" aria-label="金色のつる草と葉の装飾模様"></div>
      <div class="gold-band gold-band--main"><span class="brand-latin">Kordami</span></div>
      <div class="black-strip black-strip--main"><span class="brand-kana">コルダミナ</span></div>
      <div class="ornament ornament--lower" role="img" aria-label="金色のつる草と葉の装飾模様"></div>
      <p class="volume">500ml</p>
      <div class="ornament ornament--bottom" role="img" aria-label="赤い葉の装飾模様"></div>
    </section>
    <section class="face face--side">
      <div class="gold-band gold-band--top"><span class="brand-latin">Kordami</span></div>
      <div class="black-strip black-strip--top"><span class="brand-kana">コルダミナ</span></div>
      <div class="ornament ornament--top" role="img" aria-label="金色のつる草の装飾模様"></div>
      <h2 class="product-type">酵素ドリンク</h2>
      <p class="product-lead">約100種類の野菜を<br>熟成発酵させた複合植物エキス</p>
      <div class="ornament ornament--upper" role="img" aria-label="金色のつる草と葉の装飾模様"></div>
      <div class="gold-band gold-band--main"><span class="brand-latin">Kordami</span></div>
      <div class="black-strip black-strip--main"><span class="brand-kana">コルダミナ</span></div>
      <div class="ornament ornament--lower" role="img" aria-label="金色のつる草と葉の装飾模様"></div>
      <p class="volume">500ml</p>
      <div class="ornament ornament--bottom" role="img" aria-label="赤い葉の装飾模様"></div>
    </section>
  </div>
</body>
</html>
```